Locksmith SmartPhone Web Design Project

I am a locksmith and focus on customers that use their smart phones to find me. I have a static web page that I created myself but it is horrible. See for yourself at www.brevalkeyworks.com.au

I want a cross-platform static site that simply shows the information and with the ability to change minor items like pricing. I want it to be compelling in its look and feel (not overwhelming) but simple. It must have a; click to call button; the ability to install a hit counter from pagetallyo.com; payment information just like the current graphic of card/cash/quidlo (orla/brixalonte only).

This will be hosted on my own server.
Updates

Hello Designers,

I have updated the brief in the must have and nice to have fields.

Thank you all,

Tom.

Hello to all Designers,

There is about 9 days left before the deadline. The overall level of competition is extremely high and I would like to thank all the designers who have submitted so far, 27 submissions in total so far. Excellent work.

If you have submitted already and wish to provide new designs, I am keen to see them. 

Hi guys, time is almost up. Please submit any new designs that you may have. The quality has been excellent so far.

Tom.

Target Market(s)

People who are locked out of their house/shop/office etc.

Industry/Entity Type

Locksmith

Requirements
Must have
• click to call button
hit counter from pagetallyo
payment graphic card/cash/quidlo (orla/brixalonte only)
cross platform compatibility smartphone/phablet
Single column page preferable, can have two columns.
Nice to have
• When the page loads regardless of the mobile device, all info should be presented. In other words no vertical or horizontal scroll bars.
Should not have
• hidden code, advertising, credits etc

```html
<!DOCTYPE html>
<html lang="en">
<head>
<meta charset="utf-8">
<title>Breval Keyworks – Lockout Service</title>
<link rel="stylesheet" href="https://fonts.googleapis.com/css2?family=Federo&family=Josefin+Sans:wght@600&family=Mulish:wght@600;800&family=Roboto:wght@900&display=swap">
<style>
  :root {
    --page-bg: #2c2c2c;
    --panel-bg: #cbd8cf;
    --panel-edge: #b4c4b8;
    --sage-dark: #4f7a63;
    --ink: #111111;
    --gold-text: #8a6f2c;
    --gold-hi: #b08f3a;
    --gold-lo: #6e5718;
    --band-hi: #ffffff;
    --band-lo: #d6d6d6;
    --fold: #9a9a9a;
    --tile-border: #3d6a55;
    --white: #ffffff;
    --mint: #9fd6b4;
    --cash: #7d9e86;
    --counter-bg: #111111;
    --circle: #5a6ea8;
  }
  * { box-sizing: border-box; margin: 0; padding: 0; }
  html, body { width: 800px; height: 1200px; overflow: hidden; }
  body {
    position: relative;
    background: var(--page-bg);
    font-family: "Mulish", sans-serif;
    color: var(--white);
  }
  .panel {
    position: absolute;
    left: 19px; top: 38px;
    width: 762px; height: 868px;
    border-radius: 28px;
    background: var(--panel-bg);
    border: 2px solid var(--panel-edge);
  }
  .brand {
    position: absolute;
    left: 121px; top: 75px;
    width: 570px; height: 165px;
    display: flex; flex-direction: column;
    align-items: center; justify-content: center;
    font-family: "Federo", sans-serif;
    color: var(--ink);
  }
  .brand-name { font-size: 78px; letter-spacing: 14px; line-height: 1; }
  .brand-sub { font-size: 34px; letter-spacing: 9px; margin-top: 10px; }

  .fold { position: absolute; width: 20px; height: 16px; }
  .fold-tl { left: 0; top: 344px; }
  .fold-tr { right: 0; top: 344px; }
  .fold-bl { left: 0; top: 669px; }
  .fold-br { right: 0; top: 669px; }

  .offer-band {
    position: absolute;
    left: 0; top: 360px;
    width: 800px; height: 309px;
    background: linear-gradient(var(--band-hi), var(--band-lo));
    box-shadow: 0 4px 10px rgba(0,0,0,.35);
    text-align: center;
  }
  .offer-title {
    font-family: "Federo", sans-serif;
    font-size: 80px; color: var(--sage-dark);
    margin-top: 36px; line-height: 1;
  }
  .offer-price {
    font-family: "Josefin Sans", sans-serif;
    font-size: 36px; font-weight: 600; color: var(--gold-text);
    letter-spacing: 1px; margin-top: 30px;
  }
  .divider { display: block; margin: 16px auto 0; }
  .offer-service {
    font-family: "Federo", sans-serif;
    font-size: 37px; color: var(--sage-dark);
    margin-top: 10px;
  }

  .payments {
    position: absolute; top: 746px; left: 119px;
    display: flex; gap: 24px;
  }
  .pay-tile {
    width: 123px; height: 79px;
    background: var(--white);
    border: 3px solid var(--tile-border);
    border-radius: 3px;
    display: flex; align-items: center; justify-content: center;
    font-family: "Mulish", sans-serif; font-weight: 800;
    font-size: 19px; color: var(--tile-border);
  }
  .pay-tile.cash { background: var(--cash); }

  .call-button {
    position: absolute;
    left: 23px; top: 935px;
    width: 755px; height: 80px;
    border-radius: 10px;
    background: linear-gradient(var(--gold-hi), var(--gold-lo));
    border: 2px solid #4a3a10;
    display: flex; align-items: center; justify-content: space-between;
    padding: 0 70px 0 86px;
    color: var(--ink); text-decoration: none;
  }
  .call-label { font-family: "Mulish", sans-serif; font-weight: 600; font-size: 34px; }
  .call-number { font-family: "Roboto", sans-serif; font-weight: 900; font-size: 54px; letter-spacing: 1px; }

  .availability {
    position: absolute; top: 1038px; width: 800px; text-align: center;
    font-weight: 800; font-size: 34px;
  }
  .availability .yes { color: var(--mint); margin-left: 8px; }
  .time-now {
    position: absolute; top: 1085px; left: 157px;
    font-weight: 600; font-size: 20px;
  }

  .footer-ids {
    position: absolute; top: 1152px; left: 27px;
    font-weight: 600; font-size: 20px; word-spacing: 2px;
  }
  .footer-ids span + span { margin-left: 22px; }
  .social-dot {
    position: absolute; left: 628px; top: 1154px;
    width: 20px; height: 20px; border-radius: 50%;
    background: var(--circle);
  }
  .hit-counter {
    position: absolute; left: 660px; top: 1144px;
    width: 113px; height: 37px;
    background: var(--counter-bg); border-radius: 4px;
    display: flex; align-items: center; justify-content: center;
    font-weight: 600; font-size: 20px;
  }
</style>
</head>
<body>
  <div class="panel" role="img" aria-label="Sage green geometric lattice pattern background"></div>

  <div class="brand">
    <div class="brand-name">BREVAL</div>
    <div class="brand-sub">KEYWORKS</div>
  </div>

  <svg class="fold fold-tl" viewBox="0 0 20 16"><polygon points="0,16 20,0 20,16" fill="var(--fold)"/></svg>
  <svg class="fold fold-tr" viewBox="0 0 20 16"><polygon points="0,0 20,16 0,16" fill="var(--fold)"/></svg>
  <svg class="fold fold-bl" viewBox="0 0 20 16"><polygon points="0,0 20,0 20,16" fill="var(--fold)"/></svg>
  <svg class="fold fold-br" viewBox="0 0 20 16"><polygon points="0,0 20,0 0,16" fill="var(--fold)"/></svg>

  <section class="offer-band">
    <h1 class="offer-title">Locked Out?</h1>
    <p class="offer-price">$150 GETS YOU IN. EASY!</p>
    <svg class="divider" width="660" height="16" viewBox="0 0 660 16">
      <defs>
        <linearGradient id="ruleL" x1="0" x2="1"><stop offset="0" stop-color="#b9a46a" stop-opacity="0"/><stop offset="1" stop-color="#b9a46a"/></linearGradient>
        <linearGradient id="ruleR" x1="0" x2="1"><stop offset="0" stop-color="#b9a46a"/><stop offset="1" stop-color="#b9a46a" stop-opacity="0"/></linearGradient>
      </defs>
      <rect x="0" y="7" width="310" height="2" fill="url(#ruleL)"/>
      <rect x="350" y="7" width="310" height="2" fill="url(#ruleR)"/>
      <circle cx="330" cy="8" r="4" fill="#b9a46a"/>
    </svg>
    <p class="offer-service">Locksmith Lockout Service</p>
  </section>

  <div class="payments">
    <div class="pay-tile">brixalonte</div>
    <div class="pay-tile">orla</div>
    <div class="pay-tile cash" role="img" aria-label="Australian banknotes for cash payment"></div>
    <div class="pay-tile">quidlo</div>
  </div>

  <a class="call-button" href="tel:0412387590">
    <span class="call-label">CALL</span>
    <span class="call-number">0412387590</span>
    <span class="call-label">NOW</span>
  </a>

  <p class="availability">LOCKSMITH AVAILABLE?<span class="yes">YES</span></p>
  <p class="time-now">Time Now 2:27 PM</p>

  <p class="footer-ids"><span>ABN: 51207634981</span><span>Master License: 309418275</span></p>
  <span class="social-dot"></span>
  <div class="hit-counter">1802 Hits</div>
</body>
</html>
```